Visitenkarten-Design für Rohrreinigungsfirma
Zielgruppe
Wir sind eine Kanal.-Rohrreinigungsfirma und suchen ein hochwertiges Design, unsere Zielgruppe sind Firmenkunden,Hausverwaltungen, Architekten sowie Behörden.
Aufgabenstellung
Das Design sollte Edel aussehen. Es sollten unsere Dienstleistungen mit auf der Visitenkarte stehen (gerne auch Rückseite): grabenlose Kanalsanierung, TV-Kamerainspektion,Dichtheitsprüfung DIN EN 1610, Fräsarbeiten mit Roboter, Fräsarbeiten mit Wasserhöchstdruck 2.500 Bar,Verstopfungsbeseitigung. (Vorderseite sollte enthalten:

```html
<!DOCTYPE html>
<html lang="de">
<head>
<meta charset="UTF-8">
<title>RUVO Kanal- &amp; Rohrreinigung – Visitenkarte</title>
<link href="https://fonts.googleapis.com/css2?family=Montserrat:wght@600;700;800&family=Open+Sans:wght@400;500&display=swap" rel="stylesheet">
<style>
  :root {
    --backdrop: #e6e4e1;
    --card-white: #f8f6f2;
    --band-blue: #b7cbe0;
    --brand-navy: #2d5a8c;
    --text-dark: #3b3f44;
    --alert-red: #e2252b;
    --bullet-grey: #6c7177;
  }
  * { margin: 0; padding: 0; box-sizing: border-box; }
  html, body {
    width: 1200px;
    height: 800px;
    overflow: hidden;
    background: var(--backdrop);
  }
  .canvas {
    width: 1200px;
    height: 800px;
    display: flex;
    align-items: center;
    justify-content: center;
  }
  .business-card {
    width: 1000px;
    height: 600px;
    background: var(--card-white);
    display: flex;
    flex-direction: column;
    box-shadow: 0 6px 24px rgba(0,0,0,0.12);
  }
  .card-head {
    height: 300px;
    display: flex;
    flex-direction: column;
    align-items: center;
    justify-content: center;
    padding-top: 20px;
  }
  .brand-name {
    font-family: 'Montserrat', sans-serif;
    font-weight: 800;
    font-size: 118px;
    line-height: 1;
    letter-spacing: -2px;
    color: var(--brand-navy);
  }
  .brand-tagline {
    margin-top: 14px;
    font-family: 'Montserrat', sans-serif;
    font-weight: 700;
    font-size: 38px;
    letter-spacing: 1px;
    color: var(--text-dark);
  }
  .emergency-line {
    margin-top: 6px;
    font-family: 'Montserrat', sans-serif;
    font-weight: 600;
    font-size: 26px;
    letter-spacing: 1.5px;
    color: var(--alert-red);
  }
  .service-band {
    flex: 1;
    background: var(--band-blue);
    display: grid;
    grid-template-columns: 1fr 1fr;
    column-gap: 40px;
    padding: 56px 60px 40px 80px;
  }
  .service-list {
    list-style: none;
    display: flex;
    flex-direction: column;
    gap: 36px;
  }
  .service-item {
    display: flex;
    align-items: flex-start;
    gap: 16px;
    font-family: 'Open Sans', sans-serif;
    font-size: 29px;
    line-height: 1.2;
    color: var(--text-dark);
  }
  .service-bullet {
    flex: none;
    width: 20px;
    height: 20px;
    margin-top: 10px;
    border-radius: 50%;
    border: 3px solid var(--bullet-grey);
    display: flex;
    align-items: center;
    justify-content: center;
  }
  .service-bullet::after {
    content: "";
    width: 8px;
    height: 8px;
    border-radius: 50%;
    background: var(--bullet-grey);
  }
</style>
</head>
<body>
<div class="canvas">
  <article class="business-card">
    <header class="card-head">
      <div class="brand-name">RUVO</div>
      <div class="brand-tagline">KANAL- &amp; ROHRREINIGUNG</div>
      <div class="emergency-line">24 STUNDEN NOTDIENST</div>
    </header>
    <section class="service-band">
      <ul class="service-list">
        <li class="service-item"><span class="service-bullet"></span><span>Grabenlose Kanalsanierung</span></li>
        <li class="service-item"><span class="service-bullet"></span><span>Dichtheitsprüfung<br>DIN EN 1610</span></li>
        <li class="service-item"><span class="service-bullet"></span><span>TV-Kamerainspektion</span></li>
      </ul>
      <ul class="service-list">
        <li class="service-item"><span class="service-bullet"></span><span>Fräsarbeiten mit Roboter</span></li>
        <li class="service-item"><span class="service-bullet"></span><span>Fräsarbeiten mit Wasser-<br>höchstdruck 2.500 Bar</span></li>
        <li class="service-item"><span class="service-bullet"></span><span>Verstopfungsbeseitigung</span></li>
      </ul>
    </section>
  </article>
</div>
</body>
</html>
```